Global Weight loss program

we need a business card based in Brooklyn , NY called PeppertonRUN . Mara Dulvik Tenbrook the founder and creator of PeppertonRUN Movement. A business based around nutrition, health, Whole Foods and fitness.

Industry/Entity Type

Food Service

Contact Information for Business Card

Phone number : 718-555-0143
website www.peppertonrun.com
email : mara@peppertonrun.com

Font styles to use
Sans Serif

Requirements
Must have
• logo colors
• green black and gold
Nice to have
• must be simple and sharp.
Should not have
• pictures of items

```html
<!DOCTYPE html>
<html lang="en">
<head>
<meta charset="utf-8">
<title>PeppertonRUN Business Card</title>
<link rel="stylesheet" href="https://fonts.googleapis.com/css2?family=Oswald:wght@500&family=Ubuntu:wght@300;400;500&family=Roboto:wght@300;400&display=swap">
<style>
  :root {
    --canvas: #d6d6d6;
    --white: #ffffff;
    --ink: #2f2f2f;
    --grey-text: #8a8a8a;
    --dark: #151515;
    --green-bright: #22e02a;
    --green: #33b534;
    --green-leaf: #5bbf2a;
    --pill: #25a52c;
  }
  * { box-sizing: border-box; margin: 0; padding: 0; }
  html, body {
    width: 878px; height: 1200px; overflow: hidden;
    background: var(--canvas);
  }
  .sheet { position: relative; width: 878px; height: 1200px; }
  .card {
    position: absolute; left: 89px; width: 700px; height: 400px;
    overflow: hidden;
    box-shadow: 0 2px 6px rgba(0,0,0,0.12);
  }
  .card--front { top: 150px; background: var(--dark); }
  .card--back { top: 650px; background: var(--white); }

  .front-art { position: absolute; inset: 0; }

  .brand-mini {
    position: absolute; left: 18px; top: 118px; width: 190px;
    text-align: center;
  }
  .brand-mini .mark {
    width: 54px; height: 54px; border-radius: 50%;
    background: var(--green-leaf); margin: 0 auto 10px;
  }
  .brand-mini .name {
    font-family: "Ubuntu", sans-serif; font-weight: 400;
    font-size: 24px; color: var(--ink); letter-spacing: -0.3px;
  }
  .brand-mini .tagline {
    font-family: "Ubuntu", sans-serif; font-weight: 300;
    font-size: 7px; color: var(--grey-text); letter-spacing: 1px;
    margin-top: 2px;
  }

  .person { position: absolute; right: 26px; top: 36px; text-align: right; }
  .person .full-name {
    font-family: "Oswald", sans-serif; font-weight: 500;
    font-size: 34px; line-height: 1; color: var(--green-bright);
    text-transform: uppercase; letter-spacing: -0.5px;
  }
  .person .role {
    font-family: "Roboto", sans-serif; font-weight: 300;
    font-size: 19px; color: var(--green); letter-spacing: 1.5px;
    margin-top: 6px; word-spacing: 4px;
  }

  .contacts {
    position: absolute; left: 372px; top: 186px; width: 304px;
    list-style: none;
  }
  .contact { position: relative; height: 42px; margin-bottom: 22px; }
  .contact .pill {
    position: absolute; left: 0; top: 4px; width: 284px; height: 36px;
    background: var(--pill); border-radius: 4px;
    font-family: "Roboto", sans-serif; font-weight: 400;
    font-size: 19px; line-height: 36px; color: var(--white);
    white-space: nowrap;
    text-align: center; padding: 0 52px 0 8px;
    opacity: 0.92;
  }
  .contact .icon {
    position: absolute; right: 0; top: -3px; width: 50px; height: 50px;
  }

  .back-bar-top {
    position: absolute; left: 38px; top: 0; width: 136px; height: 16px;
    background: var(--green-leaf);
  }
  .back-band-bottom {
    position: absolute; left: 0; bottom: 0; width: 100%; height: 16px;
    background: var(--green);
  }
  .brand-main { position: absolute; left: 0; top: 62px; width: 100%; text-align: center; }
  .brand-main .mark {
    width: 150px; height: 150px; border-radius: 50%;
    background: var(--green-leaf); margin: 0 auto 14px;
  }
  .brand-main .name {
    font-family: "Ubuntu", sans-serif; font-weight: 400;
    font-size: 70px; line-height: 1; color: var(--ink); letter-spacing: -1px;
  }
  .brand-main .tagline {
    font-family: "Ubuntu", sans-serif; font-weight: 300;
    font-size: 20px; color: var(--grey-text); letter-spacing: 3px;
    margin-top: 4px;
  }
</style>
</head>
<body>
<main class="sheet">

  <section class="card card--front">
    <svg class="front-art" width="700" height="400" viewBox="0 0 700 400">
      <defs>
        <radialGradient id="dark-photo" cx="0.45" cy="0.45" r="0.7">
          <stop offset="0" stop-color="#3a3a3a"/>
          <stop offset="1" stop-color="#141414"/>
        </radialGradient>
        <linearGradient id="wedge" x1="0" y1="0" x2="1" y2="1">
          <stop offset="0" stop-color="#45ff3e"/>
          <stop offset="1" stop-color="#17b21d"/>
        </linearGradient>
      </defs>
      <rect width="700" height="400" fill="url(#dark-photo)" role="img" aria-label="Faint dark photograph of a fitness figure behind the contact details"/>
      <polygon points="0,0 178,0 240,192 112,400 0,400" fill="#ffffff"/>
      <polygon points="200,240 118,400 150,400 224,230" fill="#111111" opacity="0.7"/>
      <polygon points="226,228 150,400 210,400" fill="url(#wedge)"/>
      <rect x="0" y="40" width="236" height="20" fill="#22e02a"/>
      <rect x="0" y="60" width="236" height="5" fill="#1a9f22"/>
    </svg>

    <div class="brand-mini">
      <div class="mark"></div>
      <div class="name">PeppertonRUN</div>
      <div class="tagline">Fitness, Nutrition and Health</div>
    </div>

    <div class="person">
      <h1 class="full-name">Mara Dulvik Tenbrook</h1>
      <p class="role">Founder and Creator</p>
    </div>

    <ul class="contacts">
      <li class="contact">
        <span class="pill">718-555-0143</span>
        <svg class="icon" viewBox="0 0 50 50" aria-hidden="true">
          <circle cx="25" cy="25" r="24" fill="#2bbf30"/>
          <path d="M17 14c2-1 4 0 5 3l1 3c0 1-1 2-2 3 1 3 3 5 6 6 1-1 2-2 3-2l3 1c3 1 4 3 3 5-1 3-4 4-7 3-7-2-12-7-14-14-1-3 0-6 2-8z" fill="#155e18"/>
        </svg>
      </li>
      <li class="contact">
        <span class="pill">www.peppertonrun.com</span>
        <svg class="icon" viewBox="0 0 50 50" aria-hidden="true">
          <circle cx="25" cy="25" r="24" fill="#2bbf30"/>
          <g fill="none" stroke="#155e18" stroke-width="2.2">
            <circle cx="25" cy="25" r="13"/>
            <ellipse cx="25" cy="25" rx="6" ry="13"/>
            <line x1="12" y1="25" x2="38" y2="25"/>
            <path d="M14 18h22M14 32h22"/>
          </g>
        </svg>
      </li>
      <li class="contact">
        <span class="pill">mara@peppertonrun.com</span>
        <svg class="icon" viewBox="0 0 50 50" aria-hidden="true">
          <circle cx="25" cy="25" r="24" fill="#2bbf30"/>
          <text x="25" y="33" text-anchor="middle" font-family="Roboto, sans-serif" font-size="24" fill="#155e18">@</text>
        </svg>
      </li>
    </ul>
  </section>

  <section class="card card--back">
    <div class="back-bar-top"></div>
    <div class="brand-main">
      <div class="mark"></div>
      <div class="name">PeppertonRUN</div>
      <div class="tagline">Fitness, Nutrition and Health</div>
    </div>
    <div class="back-band-bottom"></div>
  </section>

</main>
</body>
</html>
```